Veterinary Hospital Brochure - 2 Drafts - 1 Normal and 1 Fun.

Meadowbrook Pet Hospital needs a brochure to promote our veterinary hospital. These will be delivered to local mailboxes. I would like to see atleast 2 submissions from each designer.
One submission conservative and A4 folded DL and another submission more radical and interesting with innovative folding or crazy concepts. Maybe the brochure could be designed to fold into a dog house ?
I want at least one version to be VERY SIMPLE AND INTIMATE.
Our existing website is here: http://furlane.example/ and our new website will look like this: http://trial4.pagemint.example/#home
Please use colors and images from the new website, and information from the old website. The heading font used in the new site is Qorvatype - Otter Tilt Sketchline
I want the brochure to be simple and engaging on first view, and then provide the opportunity to find more information if desired. The brochure needs to be captivating on the outside so people don't throw it away immediately.

We will soon need letterhead, flags, pens, business cards, signs and vouchers so there is the opportunity for more work for the successful designer.

Target Market(s)

Women 25 to 44

Industry/Entity Type

Veterinary

Contact Information for Business Card

Meadowbrook Pet Hospital
14 Marlow Crescent
Tamsworth Vale
NSW 2417
Phone: 02 61938205
Emergency: 0417360592
Fax: 02 83159462
www.meadowbrookvets.example
contact@meadowbrookvets.example

Font styles to use
Script

Requirements
Must have
• Colors from the new website: http://meadowbrookvets.example/ and new logo.
• Information from the old website: http://furlane.example/
• 2 drafts - A normal A4 folded DL flyer and an interesting crazy design.
Nice to have
• VERY SIMPLE
• Subdued
• Intimate
Should not have
• Intense colours
• Red

```html
<!DOCTYPE html>
<html lang="en">
<head>
<meta charset="utf-8">
<title>Meadowbrook Pet Hospital – Brochure Outside</title>
<link rel="stylesheet" href="https://fonts.googleapis.com/css2?family=Chewy&family=Poppins:wght@400;500;600;700&display=swap">
<style>
  :root{
    --green:#7aa329;
    --green-dark:#5f8a1c;
    --green-light:#a9c95a;
    --orange:#f08a2c;
    --brown:#4a2a12;
    --white:#ffffff;
    --ink:#2b2b2b;
    --page:#dcdcdc;
    --sky:#dfe9ef;
    --map:#ececec;
  }
  *{margin:0;padding:0;box-sizing:border-box}
  html,body{width:1200px;height:1200px;overflow:hidden;background:var(--page);font-family:"Poppins",sans-serif}
  .brochure{position:absolute;left:30px;top:200px;width:1140px;height:800px;display:flex;box-shadow:0 6px 24px rgba(0,0,0,.18)}
  .panel{position:relative;width:380px;height:800px;overflow:hidden}
  .panel svg.bg{position:absolute;inset:0;width:380px;height:800px}
  .about-title{position:absolute;left:100px;top:282px;font-size:26px;font-weight:600;color:var(--orange);text-decoration:underline;text-underline-offset:4px}
  .about-text{position:absolute;left:100px;top:330px;width:255px;font-size:12.5px;line-height:1.6;color:var(--ink)}
  .logo{position:absolute;left:0;width:380px;text-align:center;color:var(--brown);font-weight:600;line-height:1.15}
  .logo .mark{display:inline-block;width:16px;height:16px;border-radius:50%;background:var(--brown);margin-bottom:8px}
  .logo .name{display:block;font-size:15px;letter-spacing:2px}
  .logo .sub{display:block;font-size:28px}
  .contact{position:absolute;left:175px;top:610px;color:var(--white);font-size:12px}
  .contact h3{font-size:15px;font-weight:600;text-decoration:underline;text-underline-offset:3px;margin-bottom:12px}
  .contact li{list-style:none;display:flex;align-items:center;gap:8px;margin-bottom:6px}
  .contact svg{width:12px;height:12px;flex:none}
  .welcome{position:absolute;left:10px;top:605px;width:360px;text-align:center;color:var(--white);font-family:"Chewy",cursive;font-weight:400;line-height:1.05}
  .welcome .lead{display:block;font-size:28px}
  .welcome .big{display:block;font-size:50px;white-space:nowrap}
  .welcome .tail{display:block;font-size:32px}
  .site-pill{position:absolute;left:85px;top:760px;width:210px;height:30px;border-radius:15px;background:var(--brown);color:var(--white);font-size:13px;font-weight:600;letter-spacing:1px;display:flex;align-items:center;justify-content:center}
</style>
</head>
<body>
<main class="brochure">

  <!-- Inside flap: About -->
  <section class="panel panel-about">
    <svg class="bg" viewBox="0 0 380 800">
      <defs>
        <linearGradient id="fieldFade" x1="0" y1="0" x2="0" y2="1">
          <stop offset="0" stop-color="#8db53a"/>
          <stop offset="1" stop-color="#6f9a22"/>
        </linearGradient>
      </defs>
      <rect width="380" height="800" fill="var(--white)"/>
      <rect y="230" width="380" height="570" fill="url(#fieldFade)"/>
      <path d="M60 250 C30 340 40 500 110 570 C170 630 280 630 380 610 L380 250 Z" fill="var(--white)"/>
      <path d="M110 586 C180 646 290 638 380 618" fill="none" stroke="var(--orange)" stroke-width="5"/>
      <g role="img" aria-label="Photo of a woman stroking a tabby cat at a table">
        <circle cx="130" cy="40" r="210" fill="#d9c2a2" stroke="var(--orange)" stroke-width="10"/>
      </g>
      <g role="img" aria-label="Faded green-toned photo of a puppy giving a high five to a girl">
        <rect x="0" y="650" width="380" height="150" fill="#86b03a" opacity=".55"/>
      </g>
    </svg>
    <h2 class="about-title">About Us</h2>
    <p class="about-text">Meadowbrook Pet Hospital is a companion animal Veterinary Hospital In Tamsworth Vale. We heat Dogs, Cats, Reptiles, Rodents, Birds, and other little critters. As a companion animal only Hospital, we are dedicated to improving the wellbeing of your beloved pets. We think they are part of the family and should receive absolute best possible care.</p>
  </section>

  <!-- Back panel: map and contact -->
  <section class="panel panel-contact">
    <svg class="bg" viewBox="0 0 380 800">
      <defs>
        <linearGradient id="meadow" x1="0" y1="0" x2="0" y2="1">
          <stop offset="0" stop-color="var(--sky)"/>
          <stop offset=".55" stop-color="#eef1ea"/>
          <stop offset=".7" stop-color="#a9c95a"/>
          <stop offset="1" stop-color="#7aa329"/>
        </linearGradient>
      </defs>
      <rect width="380" height="800" fill="url(#meadow)" role="img" aria-label="Photo of a sunny sky over a grassy meadow"/>
      <g role="img" aria-label="Street map showing the hospital location">
        <circle cx="190" cy="370" r="128" fill="var(--map)" stroke="var(--orange)" stroke-width="10"/>
      </g>
      <path d="M120 610 C200 560 300 540 380 520 L380 800 L120 800 Z" fill="var(--green)"/>
      <path d="M120 600 C200 550 300 530 380 510" fill="none" stroke="var(--white)" stroke-width="10"/>
      <path d="M120 590 C200 542 300 520 380 500" fill="none" stroke="var(--orange)" stroke-width="5"/>
      <g role="img" aria-label="Photo of a smiling golden retriever puppy">
        <path d="M10 800 L10 650 C10 600 60 570 100 575 C150 580 180 620 180 670 L180 800 Z" fill="#e8d3ad"/>
      </g>
    </svg>
    <div class="logo" style="top:120px">
      <span class="mark"></span>
      <span class="name">MEADOWBROOK PET</span>
      <span class="sub">HOSPITAL</span>
    </div>
    <div class="contact">
      <h3>Meadowbrook Pet Hospital</h3>
      <ul>
        <li><svg viewBox="0 0 12 12"><path d="M2 1 L4 1 L5 4 L3.5 5 C4 6.5 5.5 8 7 8.5 L8 7 L11 8 L11 10 C11 11 10 11 9 11 C5 10 2 7 1 3 C1 2 1 1 2 1Z" fill="var(--white)"/></svg>619382, 6193MPET</li>
        <li><svg viewBox="0 0 12 12"><rect x="1" y="4" width="10" height="6" rx="1" fill="var(--white)"/><rect x="3" y="1" width="6" height="3" fill="var(--white)"/></svg>61930447</li>
        <li><svg viewBox="0 0 12 12"><rect x="1" y="3" width="10" height="7" rx="1" fill="none" stroke="var(--white)" stroke-width="1.3"/><path d="M1 3 L6 7 L11 3" fill="none" stroke="var(--white)" stroke-width="1.3"/></svg>contact@furlane.example</li>
        <li><svg viewBox="0 0 12 12"><circle cx="6" cy="6" r="5" fill="none" stroke="var(--white)" stroke-width="1.3"/><path d="M1 6 H11 M6 1 C3 4 3 8 6 11 M6 1 C9 4 9 8 6 11" fill="none" stroke="var(--white)" stroke-width="1"/></svg>www.furlane.example</li>
        <li><svg viewBox="0 0 12 12"><circle cx="6" cy="6" r="5.5" fill="var(--white)"/></svg>Meadowbrook PetHospital</li>
      </ul>
    </div>
  </section>

  <!-- Front cover -->
  <section class="panel panel-cover">
    <svg class="bg" viewBox="0 0 380 800">
      <defs>
        <linearGradient id="coverPhoto" x1="0" y1="0" x2="0" y2="1">
          <stop offset="0" stop-color="#e4ecf1"/>
          <stop offset=".35" stop-color="#efe9df"/>
          <stop offset=".7" stop-color="#8a7560"/>
          <stop offset="1" stop-color="#9fbf5a"/>
        </linearGradient>
      </defs>
      <rect width="380" height="600" fill="url(#coverPhoto)" role="img" aria-label="Photo of a woman hugging and kissing her dog in a meadow"/>
      <path d="M0 450 C120 410 280 410 380 480 L380 800 L0 800 Z" fill="var(--orange)"/>
      <path d="M0 462 C120 422 280 424 380 494 L380 800 L0 800 Z" fill="var(--white)"/>
      <path d="M0 480 C120 440 270 444 380 520 L380 800 L0 800 Z" fill="var(--green)"/>
    </svg>
    <div class="logo" style="top:40px">
      <span class="mark"></span>
      <span class="name">MEADOWBROOK PET</span>
      <span class="sub">HOSPITAL</span>
    </div>
    <h1 class="welcome">
      <span class="lead">Welcome to</span>
      <span class="big">Meadowbrook</span>
      <span class="tail">Pet Hospital</span>
    </h1>
    <div class="site-pill">www.furlane.example</div>
  </section>

</main>
</body>
</html>
```